Come crowdsource a Web Design for a brazilian crowdsource Startup!

> NAME OF OUR STARTUP:
Vantremo

> DESCRIPTION OF OUR STARTUP:
We are a crowdsourcing startup in Brazil providing consultancy and technology to support other companies to crowdsource their projects.
We also operate doing big crowdsource campaings related to polemic subjects in Brazil.

> WHAT ARE OUR TARGET AUDIENCE?
Our target audience are young people around 20-35 years old.
Generation Y (Millennial Generation)

> WHAT IS OUR INDUSTRY?
Internet, web

> WHAT DO WE NEED?
We need a Web Design for our first site.

We need 5 pages:
- Home
- What is Crowdsourcing?
- Solutions
- About Us
- Blog
- A box for the "Contact" tab (this is not a page)

Please, find attached a Layout Sketch of what I've imagined.

Lets talk about the sketch:
Well, first of all, it's a SKETCH, so you don't have to send proposals exactly as the sketch. The sketch is just to show how I've imagined the ditribution of the content boxes. For example, the menu bar doesnt need to be a rectangle exactly like the sketch, but, I would like to have the menu on the right side of the logo. Also, you will see that the boxes are all squeezed, of course I dont want them soo squeezed! Again, its juust a SKETCH!

About the images on the sketch:
IMG1 - Some nice and simple image related to collectivity or related to crowdsourcing or maybe use our O logo.

IMG2 - Some simple and creative image related to Consultancy. It doesnt need to be so obvious.

IMG3 - Some simple and creative image related to Web 2.0 Software Technology. It doesnt need to be so obvious.

IMG4 - Some simple and creative image related to a full package of Consultancy + Technology. It doesnt need to be so obvious.

IMG5 - Some nice and simple image related to collectivity or related to crowdsourcing.

IMG6 - Some nice and simple image related to Ideation. Maybe a light bulb? I dont know, be creative!

IMG7 - Some nice and simple image related to Crowdlabor. I dont know, be creative!

IMG8 - Some nice and simple image related to CrowdFeedback. Maybe a megaphone? A loudspeaker? I dont know, be creative!

IMG9 - Some nice and simple image related to us! Maybe our O logo ? I dont know, be creative!

THE CONTACT SIDE BAR - we need a nice and simple contact side bar. By the way, on the sketch this bar is shown only at the homepage, but when the site becomes real this bar will stay along all the pages.

THE CONTACT BOX - we need a nice and simple contact box.

ABOUT THE COLORS TO USE: we would like some color to our background and titles. We like colors similars to our logo: really light blue ? light green/blue ? light grey ? light orange ? I dont know, you guys knows more about that then me =)

PLIMBOOK SHARE/LIKE BUTTON: We would like a plimbook share/like button somewhere on the site!

ABOUT THE ATTACHED FILES:

ADDITIONALS:
> The name Vantremo comes from "collectivity". With our name we want to pass the idea of the collectivity from the crowdsource work model.

> Our communication is directed to the Generation Y.

> Remember, we are a Startup! So we need a modern and simple site, something like the web 2.0 trends. It must be beautiful =)

> We arent a serious company. We are a young and fun company! Please, dont come with old fashionable company sites.

> Be creative =] !

Target Market(s)

Our target audience are young people around 20-35 years old. Generation Y (Millennial Generation)

Industry/Entity Type

Communication

Requirements
Must have
• We need a Web Design for our first site.

We need 5 pages:
- Home
- What is Crowdsourcing?
- Solutions
- About Us
- Blog

ABOUT THE COLORS TO USE: we would like some color to our background and titles. We like colors similars to our logo: really light blue ? light green/blue ? light grey ? light oranges ? I dont know, you guys knows more about that then me =)

Should not have
• Poor/serious/old fashionable designs

```html
<!DOCTYPE html>
<html lang="en">
<head>
<meta charset="utf-8">
<title>Vantremo Blog</title>
<link href="https://fonts.googleapis.com/css2?family=Cuprum:ital,wght@0,400;0,700;1,400&family=Montserrat:wght@400;600;700&display=swap" rel="stylesheet">
<style>
:root{
  --orange:#f7a33c;
  --orange-deep:#e8801f;
  --ink:#2f3338;
  --muted:#6b6f73;
  --soft:#a3a6a9;
  --link:#2a94c6;
  --teal:#2aa6b8;
  --rule:#d9dadb;
  --bg:#ffffff;
  --tab:#3b3d3f;
}
*{margin:0;padding:0;box-sizing:border-box}
html,body{width:1029px;height:1200px;overflow:hidden;background:var(--bg)}
body{position:relative;font-family:"Montserrat",sans-serif;color:var(--ink)}
.abs{position:absolute}
.header{left:0;top:0;width:1029px;height:77px;background:linear-gradient(#fbfbfb,#eef0f1)}
.hero-band{left:0;top:77px;width:1029px;height:38px;background:linear-gradient(90deg,#9fc3cf,#cfe0e6 25%,#b6cfd8 55%,#dfe9ed 80%,#c3d7de)}
.brand{left:128px;top:14px;display:flex;align-items:center;gap:8px}
.brand-dot{width:40px;height:40px;border-radius:50%;background:var(--teal)}
.brand-name{font-family:"Montserrat",sans-serif;font-weight:700;font-size:34px;color:var(--teal);letter-spacing:-.5px}
.nav{left:440px;top:30px;display:flex;align-items:center;font-size:11px;font-weight:600;color:var(--ink)}
.nav a{color:inherit;text-decoration:none;padding:6px 12px;margin-left:1px}
.nav .active{background:var(--orange);color:#fff;border-radius:3px;padding:6px 13px;margin-left:8px}
.contact-tab{left:0;top:347px;width:34px;height:119px;background:var(--tab);border-radius:0 4px 4px 0;display:flex;align-items:center;justify-content:center}
.contact-tab span{transform:rotate(-90deg);color:#fff;font-size:16px;letter-spacing:1px;white-space:nowrap}
.post{left:121px;width:538px}
.date{position:absolute;left:0;top:0;width:114px;height:64px;background:var(--orange);color:#fff;font-family:"Cuprum",sans-serif;font-size:19px;text-align:center;box-shadow:3px 0 0 #eee}
.date div{height:32px;line-height:34px}
.date div:first-child{border-bottom:1px solid rgba(255,255,255,.45)}
.post-title{position:absolute;left:134px;top:-6px;font-family:"Cuprum",sans-serif;font-weight:400;font-size:27px;color:var(--ink);white-space:nowrap}
.post-body{position:absolute;left:134px;top:36px;width:410px;font-size:12.4px;line-height:20.1px}
.post-body p+p{margin-top:20px}
.meta{position:absolute;left:134px;top:316px;font-size:11px;color:var(--muted)}
.meta .sep{margin:0 12px}
.share{position:absolute;left:134px;top:346px;display:flex;align-items:center;font-size:11px;color:var(--link)}
.share svg{margin-right:4px}
.share .comments{margin-right:10px}
.dot{width:18px;height:18px;border-radius:50%;margin-right:8px}
.dot.a{background:#2b4f86}.dot.b{background:#3aa9de}.dot.c{background:#c42c26}
.divider{left:120px;top:557px;width:539px;height:1px;background:var(--rule)}
.vrule{left:699px;top:159px;width:1px;height:835px;background:var(--rule)}
.sidebar{left:740px;top:159px;width:170px}
.side-title{font-family:"Cuprum",sans-serif;font-size:20px;color:var(--ink)}
.year{font-weight:700;font-size:12.5px;margin-top:12px}
.months a{display:block;color:var(--link);text-decoration:none;font-size:12.5px;line-height:20px}
.tags{position:relative;height:130px;margin-top:14px}
.tags span{position:absolute;white-space:nowrap}
.footer-line{left:0;top:1080px;width:1029px;height:2px;background:linear-gradient(90deg,#f6c79b,#f0a460 30%,#f8d3b1 60%,#f0a460)}
.footer{left:121px;top:1096px;width:788px;height:36px;display:flex;align-items:center;font-family:"Cuprum",sans-serif;font-style:italic;color:var(--muted)}
.footer .col{border-right:1px solid #8a8d90;height:27px;display:flex;align-items:center;padding:0 19px;font-size:16px}
.quick{padding-left:0!important;flex-direction:column;align-items:flex-start!important;justify-content:center}
.quick b{font-weight:400;font-size:16px}
.quick small{font-style:normal;font-family:"Montserrat",sans-serif;font-size:9.5px;color:var(--orange-deep)}
.subscribe{padding-left:21px;font-size:16px}
.subscribe .field{width:186px;height:16px;background:#e3e4e5;margin-top:1px;position:relative;border:1px solid #d4d5d6}
.subscribe .go{position:absolute;right:3px;top:1px;width:12px;height:12px;background:var(--orange-deep)}
.bottom-band{left:0;top:1143px;width:1029px;height:7px;background:var(--orange-deep)}
.copyright{left:121px;top:1164px;font-size:10px;color:var(--ink)}
.like{left:780px;top:1161px;display:flex;align-items:center;font-size:9px;color:#3b5998}
.like .btn{border:1px solid #9aa;border-radius:2px;padding:2px 5px;background:#eef0f5;margin-right:5px;font-size:9px}
.like .sq{width:10px;height:10px;background:#3b5998;margin-right:4px}
</style>
</head>
<body>
<div class="abs header"></div>
<div class="abs hero-band" role="img" aria-label="Soft blurred photographic band of a crowd"></div>

<div class="abs brand"><div class="brand-dot"></div><div class="brand-name">Vantremo</div></div>

<nav class="abs nav">
  <a>HOME</a><a>WHAT IS CROWDSOURCING?</a><a>SOLUTIONS</a><a>ABOUT US</a><a class="active">BLOG</a>
</nav>

<div class="abs contact-tab"><span>CONTACT</span></div>

<article class="abs post" style="top:159px">
  <div class="date"><div>21/02/2013</div><div>FRIDAY</div></div>
  <h2 class="post-title">Haiti and the Power of Crowdsourcing</h2>
  <div class="post-body">
    <p>It's been two weeks since I called Marco Telvane to launch Mapwise's crisis mapping platform in Haiti. I could probably write 100 blog posts on the high's and low's of the past 14 days. Perhaps there will more time be next month to recount the first two weeks of the disaster response. For now, I wanted to share an astounding example of crowdsourcing that took place 10 days ago.</p>
    <p>Lorem ipsum dolor sit amet, consectetur adipiscing elit. Donec lacinia semper justo vitae mollis. Mauris iaculis mi et magna elementum vitae feugiat augue luctus. Lorem ipsum dolor sit amet, consectetur adipiscing elit. Praesent viverra viverra lectus eu elementum. In vel tellus magna. Fusce</p>
  </div>
  <div class="meta">By: Rui Danzo<span class="sep">|</span>Tags: Haiti, crowdsourcing, contest</div>
  <div class="share">
    <svg width="11" height="10" viewBox="0 0 11 10"><path d="M1 1h9v6H5L2 9V7H1z" fill="none" stroke="currentColor"/></svg>
    <span class="comments">2 Comments</span>
    <span class="dot a"></span><span class="dot b"></span><span class="dot c"></span>
  </div>
</article>

<div class="abs divider"></div>

<article class="abs post" style="top:596px">
  <div class="date"><div>21/02/2013</div><div>FRIDAY</div></div>
  <h2 class="post-title">Haiti and the Power of Crowdsourcing</h2>
  <div class="post-body">
    <p>It's been two weeks since I called Marco Telvane to launch Mapwise's crisis mapping platform in Haiti. I could probably write 100 blog posts on the high's and low's of the past 14 days. Perhaps there will more time be next month to recount the first two weeks of the disaster response. For now, I wanted to share an astounding example of crowdsourcing that took place 10 days ago.</p>
    <p>Lorem ipsum dolor sit amet, consectetur adipiscing elit. Donec lacinia semper justo vitae mollis. Mauris iaculis mi et magna elementum vitae feugiat augue luctus. Lorem ipsum dolor sit amet, consectetur adipiscing elit. Praesent viverra viverra lectus eu elementum. In vel tellus magna. Fusce</p>
  </div>
  <div class="meta">By: Rui Danzo<span class="sep">|</span>Tags: Haiti, crowdsourcing, contest</div>
  <div class="share">
    <svg width="11" height="10" viewBox="0 0 11 10"><path d="M1 1h9v6H5L2 9V7H1z" fill="none" stroke="currentColor"/></svg>
    <span class="comments">2 Comments</span>
    <span class="dot a"></span><span class="dot b"></span><span class="dot c"></span>
  </div>
</article>

<div class="abs vrule"></div>

<aside class="abs sidebar">
  <h3 class="side-title">Archive</h3>
  <div class="year">2013</div>
  <div class="months"><a>January (5)</a></div>
  <div class="year" style="margin-top:20px">2012</div>
  <div class="months"><a>December (5)</a><a>November (6)</a><a>October (3)</a></div>
  <h3 class="side-title" style="margin-top:36px">Tags</h3>
  <div class="tags">
    <span style="left:0;top:0;font-size:20px;font-weight:700">Crowdsourcing</span>
    <span style="left:34px;top:30px;font-size:12px;color:var(--soft)">branding</span>
    <span style="left:102px;top:38px;font-size:12px;font-weight:700">Brasil</span>
    <span style="left:0;top:46px;font-size:16px;color:var(--muted)">Startup</span>
    <span style="left:63px;top:60px;font-size:14px;color:var(--soft)">engaging</span>
    <span style="left:3px;top:79px;font-size:11.5px;font-weight:700">Crowdfunding</span>
    <span style="left:81px;top:102px;font-size:12px;color:var(--muted)">Crowdlabor</span>
  </div>
</aside>

<div class="abs footer-line"></div>
<footer class="abs footer">
  <div class="col quick"><b>Quick and Positive Response</b><small>+00.123.456.7890 | +00.123.456.9990</small></div>
  <div class="col">About Us</div>
  <div class="col">What is Crowdsourcing?</div>
  <div class="col">Solutions</div>
  <div class="subscribe">Subscribe Newsletter<div class="field"><span class="go"></span></div></div>
</footer>
<div class="abs bottom-band"></div>
<div class="abs copyright">Copyright 2013, All rights reserved.</div>
<div class="abs like"><span class="btn">Like</span><span class="sq"></span>10 people like this.</div>
</body>
</html>
```